Create Web Design Template with Source Files

I need a web design built with PSD/source files. See attached design I have made to guidance. Also I have attached an image I have used so you can use it.

I got my inspiration from this site if you would like to use it also:
http://trelvix.com/home

PSD & html slicing and responsive designs also. So we can run across all devices.

Number of Pages Required

1 page

Requirements
Must have
• See attachments. Ask if you have any questions...

```html
<!DOCTYPE html>
<html lang="en">
<head>
<meta charset="utf-8">
<title>Quarrelo — Debate is Life</title>
<link href="https://fonts.googleapis.com/css2?family=Josefin+Sans:wght@400;600&family=Tinos:ital@0;1&display=swap" rel="stylesheet">
<style>
:root{
  --page:#ffffff;
  --ink:#1e1e1e;
  --muted:#555555;
  --gold:#b08a4f;
  --gold-dark:#9a7842;
  --rule:#cfcfcf;
  --dark:#1b1b1b;
  --darker:#141414;
  --hero-a:#3b2f2a;
  --hero-b:#6a5446;
  --field:#e6e6e6;
  --dim:rgba(0,0,0,.4);
  --sans:'Josefin Sans',Arial,sans-serif;
  --serif:'Tinos','Times New Roman',serif;
}
*{box-sizing:border-box;margin:0;padding:0}
html,body{width:667px;height:1200px;overflow:hidden}
body{position:relative;background:var(--page);font-family:var(--sans);color:var(--ink)}
.abs{position:absolute}
.site-header{left:0;top:0;width:667px;height:104px;background:var(--page)}
.social{display:flex;gap:4px}
.social span{width:11px;height:11px;border:1px solid currentColor;border-radius:50%;display:block}
.header-social{left:136px;top:46px;color:var(--ink)}
.wordmark{font-family:var(--sans);font-weight:600;color:var(--ink)}
.header-mark{left:274px;top:38px;width:120px;text-align:center;font-size:26px}
.hero{left:0;top:104px;width:667px;height:174px;background:linear-gradient(90deg,var(--hero-a),var(--hero-b) 50%,var(--hero-a))}
.hero-title{left:0;top:160px;width:667px;text-align:center;font-family:var(--serif);color:#eee;font-size:30px}
.hero-sub{left:0;top:193px;width:667px;text-align:center;font-family:var(--serif);color:#ddd;font-size:17px}
.post-title{font-family:var(--serif);font-size:15px;color:var(--ink)}
.post-date{font-family:var(--serif);font-style:italic;font-size:6px;color:var(--gold);display:flex;align-items:center;gap:8px}
.post-date::before,.post-date::after{content:"";width:18px;height:1px;background:var(--gold)}
.photo{display:block}
.card-title{font-family:var(--serif);font-size:8px}
.card-text{font-size:5px;line-height:8.5px;color:var(--muted)}
.btn{font-family:var(--serif);font-size:6px;text-align:center;color:#fff;background:var(--gold);display:flex;align-items:center;justify-content:center}
.btn-ghost{background:var(--page);color:var(--gold);border:1px solid var(--rule)}
.older{left:300px;top:1035px;width:96px;text-align:right;font-size:5.5px;font-weight:600}
.widget{border:1px solid #e4e4e4;background:var(--page)}
.widget-head{font-size:5.5px;text-align:center;letter-spacing:.3px}
.logo-box{background:var(--dark);display:flex;align-items:center;justify-content:center;color:#eee;font-family:var(--sans);font-weight:600;font-size:18px}
.blurb{font-size:5px;line-height:7.5px}
.sign{height:6px;background:linear-gradient(90deg,transparent,#8a8a8a,transparent)}
.newsletter{background:var(--dark);color:#eee}
.field{background:var(--field);font-family:var(--serif);font-style:italic;font-size:5px;color:#999;display:flex;align-items:center;justify-content:center}
.cat-list{list-style:none}
.cat-list li{font-size:5px;padding:3px 0 3px 6px;border-bottom:1px solid #e4e4e4;height:12.5px}
.site-footer{left:0;top:1058px;width:667px;height:142px;background:var(--darker);color:var(--gold)}
.foot-head{font-family:var(--serif);font-size:7px}
.foot-item{font-size:5.5px}
.foot-date{font-size:5px;color:#ddd}
.copyright{left:0;top:1186px;width:667px;text-align:center;font-size:4.5px;color:#ccc}
.dim{left:0;top:0;width:667px;height:1200px;background:var(--dim)}
.menu-panel{left:406px;top:0;width:126px;height:278px;background:var(--page)}
.menu-item{left:11px;width:104px;height:13px;border-bottom:1px solid #bbb;font-size:5px;font-weight:600;display:flex;align-items:center;justify-content:space-between;padding:0 4px 0 5px}
.menu-item svg{width:5px;height:5px}
</style>
</head>
<body>
<header class="abs site-header">
  <div class="abs social header-social"><span></span><span></span><span></span><span></span><span></span></div>
  <div class="abs wordmark header-mark">Quarrelo</div>
</header>
<section class="abs hero" role="img" aria-label="Photo of an excited crowd cheering"></section>
<div class="abs hero-title">Debate is LIFE</div>
<div class="abs hero-sub">The rest is just prep-time</div>

<main>
  <div class="abs post-title" style="left:136px;top:308px;width:260px;text-align:center">Lorem is Ipsum</div>
  <div class="abs post-date" style="left:136px;top:327px;width:260px;justify-content:center">July 22, 2017</div>
  <div class="abs photo" style="left:135px;top:338px;width:261px;height:126px;background:linear-gradient(180deg,#3a2a20,#5a4330 60%,#2a1f18)" role="img" aria-label="Photo of a vaulted old library hall"></div>
  <div class="abs card-title" style="left:136px;top:474px">Why do we use it?</div>
  <p class="abs card-text" style="left:136px;top:485px;width:258px">It is a long established fact that a reader will be distracted by the readable content of a page when looking at its layout. The point of using Lorem Ipsum is that it has a more-or-less normal distribution of letters, as opposed to using 'Content here, content here', making it look like readable English.</p>
  <div class="abs btn btn-ghost" style="left:136px;top:518px;width:90px;height:18px;font-style:italic">Start Debate</div>
  <div class="abs btn" style="left:238px;top:518px;width:90px;height:18px">Give Your Opinion</div>

  <div class="abs post-title" style="left:136px;top:550px">Where does it from?</div>
  <div class="abs post-date" style="left:136px;top:569px">September 19, 2017</div>
  <div class="abs photo" style="left:135px;top:580px;width:126px;height:126px;background:linear-gradient(180deg,#5a5a5a,#9a9a9a 45%,#3a3a3a)" role="img" aria-label="Black and white photo of a mushroom cloud over the sea"></div>
  <div class="abs photo" style="left:271px;top:580px;width:125px;height:126px;background:linear-gradient(160deg,#4a4a48,#2a2a28 60%,#6a4a2a)" role="img" aria-label="Photo of a firefighter pointing"></div>
  <div class="abs card-title" style="left:136px;top:715px">Where does it come from?</div>
  <p class="abs card-text" style="left:136px;top:727px;width:124px">It is a long established fact that a reader will be distracted by the readable content of a page when looking at its layout.</p>
  <div class="abs card-title" style="left:271px;top:715px">Where can I get some?</div>
  <p class="abs card-text" style="left:271px;top:727px;width:124px">It is a long established fact that a reader will be distracted by the readable content of a page when looking at its layout.</p>
  <div class="abs btn" style="left:135px;top:761px;width:57px;height:17px">Start Debate</div>
  <div class="abs btn" style="left:203px;top:761px;width:57px;height:17px">Give Your Opinion</div>
  <div class="abs btn" style="left:271px;top:761px;width:57px;height:17px">Start Debate</div>
  <div class="abs btn" style="left:339px;top:761px;width:57px;height:17px">Give Your Opinion</div>

  <div class="abs post-title" style="left:136px;top:792px">Where does it from?</div>
  <div class="abs post-date" style="left:136px;top:811px">September 19, 2017</div>
  <div class="abs photo" style="left:135px;top:822px;width:126px;height:125px;background:linear-gradient(180deg,#8a9aaa,#c8ccd0 60%,#9aa0a6)" role="img" aria-label="Photo of a vintage biplane in a hangar"></div>
  <div class="abs photo" style="left:271px;top:822px;width:125px;height:125px;background:linear-gradient(180deg,#2a241e,#4a3e30 60%,#1e1a16)" role="img" aria-label="Photo of two soldiers at a table"></div>
  <div class="abs card-title" style="left:136px;top:957px">Where does it come from?</div>
  <p class="abs card-text" style="left:136px;top:969px;width:124px">It is a long established fact that a reader will be distracted by the readable content of a page when looking at its layout.</p>
  <div class="abs card-title" style="left:271px;top:957px">Where can I get some?</div>
  <p class="abs card-text" style="left:271px;top:969px;width:124px">It is a long established fact that a reader will be distracted by the readable content of a page when looking at its layout.</p>
  <div class="abs btn" style="left:135px;top:1002px;width:57px;height:17px">Start Debate</div>
  <div class="abs btn" style="left:203px;top:1002px;width:57px;height:17px">Give Your Opinion</div>
  <div class="abs btn" style="left:271px;top:1002px;width:57px;height:17px">Start Debate</div>
  <div class="abs btn" style="left:339px;top:1002px;width:57px;height:17px">Give Your Opinion</div>
  <div class="abs older">OLDER POSTS&gt;&gt;&gt;</div>
</main>

<aside>
  <div class="abs widget" style="left:406px;top:312px;width:125px;height:125px">
    <div class="abs widget-head" style="left:0;top:11px;width:123px">ABOUT</div>
    <div class="abs logo-box" style="left:10px;top:24px;width:104px;height:52px">Quarrelo</div>
    <p class="abs blurb" style="left:10px;top:86px;width:106px">Aenean commodo ligula eget dolor. Aenean massa. Cum sociis natoque penatibus.</p>
    <div class="abs sign" style="left:42px;top:106px;width:40px" role="img" aria-label="Handwritten signature"></div>
  </div>
  <div class="abs newsletter" style="left:406px;top:454px;width:125px;height:74px">
    <div class="abs widget-head" style="left:0;top:11px;width:125px">SUBSCRIBE TO MY NEWSLETTER</div>
    <div class="abs field" style="left:11px;top:26px;width:104px;height:13px">Your Email Address</div>
    <div class="abs" style="left:11px;top:49px;width:104px;height:13px;background:#8f8f8f;font-size:5px;font-weight:600;display:flex;align-items:center;justify-content:center;color:#222">SUBSCRIBE</div>
  </div>
  <div class="abs widget" style="left:406px;top:546px;width:125px;height:120px">
    <div class="abs widget-head" style="left:0;top:9px;width:123px">CATEGORIES</div>
    <ul class="abs cat-list" style="left:10px;top:20px;width:104px">
      <li>Art</li><li>Food</li><li>Lifestyle</li><li>Movie</li><li>Music</li><li>Top</li><li>Travel</li>
    </ul>
  </div>
</aside>

<footer class="abs site-footer">
  <div class="abs wordmark" style="left:135px;top:24px;font-size:16px;color:#eee">Quarrelo</div>
  <div class="abs foot-head" style="left:135px;top:48px">Connect With Us On :</div>
  <div class="abs social" style="left:135px;top:60px;color:#bbb"><span></span><span></span><span></span><span></span><span></span></div>
  <div class="abs foot-head" style="left:135px;top:80px">Subscribe to Debate :</div>
  <div class="abs field" style="left:135px;top:92px;width:91px;height:12px;background:#262626;justify-content:flex-start;padding-left:5px;color:#666">Email Address</div>
  <div class="abs" style="left:226px;top:92px;width:35px;height:12px;background:var(--gold);display:flex;align-items:center;justify-content:center">
    <svg width="8" height="7" viewBox="0 0 8 7"><path d="M0 3.5L8 0 6 7 4 4.5z" fill="#fff"/></svg>
  </div>
  <div class="abs foot-head" style="left:271px;top:30px">Recent Debates</div>
  <div class="abs foot-item" style="left:271px;top:53px">BEAUTY OF NATURE</div>
  <div class="abs foot-date" style="left:271px;top:63px">July 22, 2015</div>
  <div class="abs foot-item" style="left:271px;top:74px">FASHION MODEL SHOOT</div>
  <div class="abs foot-date" style="left:271px;top:84px">July 22, 2015</div>
  <div class="abs foot-item" style="left:271px;top:94px">GOLDEN SNOW LAND</div>
  <div class="abs foot-date" style="left:271px;top:105px">July 22, 2015</div>
  <div class="abs foot-head" style="left:406px;top:30px">Most Popular Opinions</div>
  <div class="abs foot-item" style="left:406px;top:53px">TOP 10 INGREDIENTS</div>
  <div class="abs foot-date" style="left:406px;top:63px">July 22, 2015</div>
  <div class="abs foot-item" style="left:406px;top:74px">FAMILY COMES FIRST</div>
  <div class="abs foot-date" style="left:406px;top:84px">July 22, 2015</div>
  <div class="abs foot-item" style="left:406px;top:94px">GOLDEN SNOW LAND</div>
  <div class="abs foot-date" style="left:406px;top:105px">July 22, 2015</div>
  <div class="abs" style="left:0;top:123px;width:667px;height:1px;background:var(--gold-dark)"></div>
</footer>
<div class="abs copyright">© Copyright Quarrelo 2018. All Rights Reserved. Privacy | Policy.</div>

<div class="abs dim"></div>

<nav class="abs menu-panel">
  <div class="abs" style="left:11px;top:10px;width:91px;height:12px;background:var(--field)"></div>
  <svg class="abs" style="left:89px;top:12px" width="9" height="9" viewBox="0 0 9 9"><circle cx="3.7" cy="3.7" r="2.8" fill="none" stroke="#333"/><path d="M5.8 5.8L8.5 8.5" stroke="#333"/></svg>
  <svg class="abs" style="left:108px;top:11px" width="10" height="10" viewBox="0 0 10 10"><path d="M1 1L9 9M9 1L1 9" stroke="#111" stroke-width="2"/></svg>
  <div class="abs menu-item" style="top:28px;border-top:1px solid #bbb">HOME<svg viewBox="0 0 5 5"><path d="M1 0.5L3.5 2.5 1 4.5" fill="none" stroke="#111"/></svg></div>
  <div class="abs menu-item" style="top:42px">ABOUT<svg viewBox="0 0 5 5"><path d="M0.5 1.5L2.5 3.5 4.5 1.5" fill="none" stroke="#111"/></svg></div>
  <div class="abs logo-box" style="left:11px;top:56px;width:104px;height:52px">Quarrelo</div>
  <p class="abs blurb" style="left:11px;top:119px;width:106px">Aenean commodo ligula eget dolor. Aenean massa. Cum sociis natoque penatibus.</p>
  <div class="abs sign" style="left:43px;top:140px;width:40px" role="img" aria-label="Handwritten signature"></div>
  <div class="abs menu-item" style="top:155px;border-top:1px solid #bbb">HOW IT WORKS<svg viewBox="0 0 5 5"><path d="M1 0.5L3.5 2.5 1 4.5" fill="none" stroke="#111"/></svg></div>
  <div class="abs menu-item" style="top:171px">WEAPONS OF COMMENT<svg viewBox="0 0 5 5"><path d="M1 0.5L3.5 2.5 1 4.5" fill="none" stroke="#111"/></svg></div>
  <div class="abs menu-item" style="top:187px;border-bottom:none">SUBSCRIBE TO OUR NEWSLETTER</div>
  <div class="abs field" style="left:11px;top:206px;width:104px;height:14px">Your Email Address</div>
  <div class="abs" style="left:11px;top:230px;width:104px;height:14px;background:var(--dark);color:#fff;font-size:5px;font-weight:600;display:flex;align-items:center;justify-content:center">SUBSCRIBE</div>
  <div class="abs" style="left:11px;top:249px;font-size:5px;font-weight:600">CONNECT ON :</div>
  <div class="abs social" style="left:27px;top:259px;color:#111"><span></span><span></span><span></span><span></span><span></span></div>
</nav>
</body>
</html>
```